Menu Design for Indian Restaurant

We are a new Indian restaurant, named Spices of Sarani Restaurant, looking for a sophisticated looking menu. It is a semi-formal dining restaurant with wooden tables and chairs and will have a focus on a creating a lively atmosphere. Environment-friendly products will be used, and the menu will be 100% vegetarian. There will be an emphasis on fresh, healthy and delicious food. We will be targeting vegans, vegetarians, health conscious people, people from all age groups, Indians, Australian's as well as other ethnic communities. We need a clean, simple, sophisticated design for the new restaurant menu. Attached is the restaurant logo for reference.

UPDATE:
- We have attached the menu
- We are not looking for any particular type of layout or size (open to suggests). Please suggest this after having a look at the menu contents. However, we will be having one formal menu to be used in the restaurant, and one in brochure form for distribution.
- There are no images at present. If you feel the need of images, please use sample images for now.

Thank you for the entries thus far.
Updates

Target Market(s)

All age groups from different nationalities

Industry/Entity Type

Indian Restaurant

Colors

Designer to choose colors to be used in the design.

Requirements
Nice to have
• This will be printed on environmentally friendly paper.

```html
<!DOCTYPE html>
<html lang="en">
<head>
<meta charset="utf-8">
<title>Spices of Sarani Restaurant – Menu</title>
<link href="https://fonts.googleapis.com/css2?family=Oleo+Script:wght@400;700&family=Open+Sans:wght@400;600;700&family=Kaushan+Script&display=swap" rel="stylesheet">
<style>
:root{
  --backdrop:#ececec;
  --saffron:#f2a03a;
  --saffron-soft:#fbe2b4;
  --cream:#fdf8ec;
  --leaf-soft:#d7eac2;
  --leaf:#3f9a3c;
  --leaf-deep:#2c7a30;
  --bark:#8b5a2b;
  --ink:#4a3a2a;
  --muted:#666;
  --rule:#a99a7c;
}
*{box-sizing:border-box}
html,body{margin:0;width:1200px;height:1200px;overflow:hidden;background:var(--backdrop);font-family:'Open Sans',sans-serif}
.spread{position:absolute;width:800px;height:570px;display:flex;box-shadow:0 8px 24px rgba(0,0,0,.18)}
.spread--outer{left:30px;top:20px}
.spread--inner{left:370px;top:610px}
.page{width:400px;height:570px;position:relative;padding:12px 12px 10px;display:flex;gap:12px;overflow:hidden;
  background:linear-gradient(180deg,var(--saffron) 0%,var(--saffron-soft) 28%,var(--cream) 52%,var(--leaf-soft) 80%,#8cc56a 100%)}
.page--left{box-shadow:inset -10px 0 14px -10px rgba(0,0,0,.25)}
.column{flex:1;display:flex;flex-direction:column;min-width:0}
.section-title{background:var(--bark);color:#fff;font-family:'Oleo Script',cursive;text-align:center;font-size:13px;line-height:1.05;padding:4px 6px;margin:4px 14px 3px}
.section-note{font-size:6px;font-style:italic;color:var(--muted);text-align:center;margin:0 0 3px;line-height:1.2}
.item{display:grid;grid-template-columns:1fr auto;column-gap:4px;border-bottom:1px dotted var(--rule);padding:1px 0 1px}
.item-name{font-family:'Oleo Script',cursive;color:var(--leaf-deep);font-size:9px;line-height:1.1}
.item-price{font-size:7.5px;color:var(--ink);align-self:end}
.item-desc{grid-column:1/-1;font-size:5.2px;color:var(--muted);line-height:1.15}
/* tighter rhythm for the long breakfast page */
.page--dense{padding-top:8px;padding-bottom:6px}
.page--dense .section-title{margin:2px 14px 2px;padding:3px 6px}
.page--dense .section-note{margin-bottom:2px}
.page--dense .item{padding:0}
.page--dense .item-name{line-height:1.05}
.page--dense .item-desc{line-height:1.1}
.page--dense .dish{margin:4px 0}
.dish{align-self:center;border-radius:50%;margin:6px 0;background:radial-gradient(circle,#e0703a 0%,#c9482a 45%,#f4f1ea 60%,#fff 100%);box-shadow:0 3px 6px rgba(0,0,0,.2)}
.dish--green{background:radial-gradient(circle,#f0c64a 0%,#d9a730 45%,#f4f1ea 60%,#fff 100%)}
.dish--brown{background:radial-gradient(circle,#7a4a2a 0%,#5c3420 45%,#f4f1ea 60%,#fff 100%)}
.spacer{flex:1}
/* cover */
.page--cover{flex-direction:column;align-items:center;padding-top:24px}
.cover-motif{width:200px;height:150px;border-radius:100px 100px 6px 6px;background:linear-gradient(180deg,#fff7e8,#f6dcae)}
.brand-name{font-family:'Open Sans',sans-serif;font-weight:700;color:#1f1f1f;font-size:21px;margin-top:10px;text-align:center}
.menu-row{display:flex;align-items:center;gap:16px;margin-top:40px}
.utensil{width:26px;height:210px;border-radius:13px;background:linear-gradient(180deg,#5aae4b,#2f8a35)}
.menu-word{font-family:'Kaushan Script',cursive;color:var(--leaf);font-size:84px;line-height:1}
.veg-label{font-family:'Oleo Script',cursive;color:var(--leaf);font-size:22px;margin-top:-70px;text-align:center;line-height:1.05}
.veg-label strong{display:block;font-size:20px}
</style>
</head>
<body>

<section class="spread spread--outer">
  <article class="page page--left page--dense">
    <div class="column">
      <h2 class="section-title">Breakfast<br>(nasta)</h2>
      <p class="section-note">Dosa, Vada, Idly served with sambar, coconut chutney and tomato chilli chutney</p>
      <div class="item"><span class="item-name">Rava Dosa</span><span class="item-price">9.9</span><span class="item-desc">Crispy crepe made with ground rice and lentils, gluten free</span></div>
      <div class="item"><span class="item-name">Kanda Rava Dosa</span><span class="item-price">11.9</span><span class="item-desc">Crispy crepe with ground rice, lentil and onion</span></div>
      <div class="item"><span class="item-name">Masala Rava Dosa</span><span class="item-price">11.9</span><span class="item-desc">Crispy crepe of ground rice and lentil stuffed with potatoes</span></div>
      <div class="item"><span class="item-name">Plain Dosa</span><span class="item-price">9.9</span><span class="item-desc">Crispy crepe made with rice and lentil batter with butter</span></div>
      <div class="item"><span class="item-name">Masala Dosa</span><span class="item-price">11.9</span><span class="item-desc">Rice and lentil batter crepe stuffed with potatoes</span></div>
      <div class="item"><span class="item-name">Vada Sambar</span><span class="item-price">7.9</span><span class="item-desc">Lentil dumpling deep fry</span></div>
      <div class="item"><span class="item-name">Thair Bara</span><span class="item-price">7.9</span><span class="item-desc">Lentil dumpling deep fry in yogurt buttermilk</span></div>
      <div class="item"><span class="item-name">Idly</span><span class="item-price">7.9</span><span class="item-desc">Dumpling of black lentil and rice, steamed</span></div>
      <div class="item"><span class="item-name">Sev Batata Puri (6)</span><span class="item-price">5.9</span><span class="item-desc">Fried puff balls with potatoes, onion, yogurt, date and mint chutney</span></div>
      <div class="item"><span class="item-name">Bhel Puri</span><span class="item-price">6.9</span><span class="item-desc">Rice puff, fresh green chilli, red onion, tomatoes, coriander</span></div>
      <h2 class="section-title">Breakfast<br>(shubhparvhat)</h2>
      <div class="item"><span class="item-name">Batata Pao (2)</span><span class="item-price">7.9</span></div>
      <div class="item"><span class="item-name">Puri Bhaji (4)</span><span class="item-price">7.9</span></div>
      <div class="item"><span class="item-name">Pao Bhaji (2)</span><span class="item-price">7.9</span></div>
      <div class="item"><span class="item-name">Aloo Parantha (2)</span><span class="item-price">7.9</span><span class="item-desc">With yogurt, pickle</span></div>
      <div class="item"><span class="item-name">Gobhi Paarantha (2)</span><span class="item-price">7.9</span><span class="item-desc">With yogurt, pickle</span></div>
      <div class="item"><span class="item-name">Muli Parantha (2)</span><span class="item-price">7.9</span><span class="item-desc">With yogurt, pickle</span></div>
      <div class="item"><span class="item-name">Thepla (4)</span><span class="item-price">7.9</span><span class="item-desc">With yogurt, pickle</span></div>
      <div class="item"><span class="item-name">Vati Khaman Dhokla (4)</span><span class="item-price">6.9</span><span class="item-desc">Fluffy soft cake, soak and crushed lentil</span></div>
      <div class="item"><span class="item-name">Kachori Aloo Sabji</span><span class="item-price">7.9</span><span class="item-desc">Stuffed legume with potato curry</span></div>
      <div class="item"><span class="item-name">Uttapam (2)</span><span class="item-price">6.9</span><span class="item-desc">Tomato, onion, chilli, coriander, sambar, chutney</span></div>
      <div class="item"><span class="item-name">Dhai Jalebi</span><span class="item-price">4.9</span><span class="item-desc">With yogurt</span></div>
      <div class="item"><span class="item-name">Musli Yogurt Fruit</span><span class="item-price">5.9</span></div>
      <div class="item"><span class="item-name">Oats</span><span class="item-price">5.9</span><span class="item-desc">Warm milk, banana</span></div>
      <div class="item"><span class="item-name">Waffle</span><span class="item-price">6.9</span><span class="item-desc">Cream, chocolate, fruit</span></div>
      <div class="item"><span class="item-name">Vegetarian Sandwich</span><span class="item-price">5.9</span><span class="item-desc">Cucumber, tomato, cheese</span></div>
      <div class="item"><span class="item-name">Masala Noodles</span><span class="item-price">7.9</span><span class="item-desc">Topped with chopped cucumbers, tomato, onion</span></div>
    </div>
    <div class="column">
      <h2 class="section-title">Soup Of The Day</h2>
      <div class="item"><span class="item-name">Cream of tomato with crotons</span><span class="item-price">4.9</span></div>
      <div class="item"><span class="item-name">Curried pumpkin with shallots</span><span class="item-price">4.9</span></div>
      <div class="dish" style="width:100px;height:70px" role="img" aria-label="Photo of a bowl of tomato soup"></div>
      <h2 class="section-title">Entrée<br>(tapas)</h2>
      <div class="item"><span class="item-name">Kamal Kofta (4pcs)</span><span class="item-price">6.9</span><span class="item-desc">Crispy potatoes, curry leaves, lotus stem, ginger, coriander</span></div>
      <div class="item"><span class="item-name">Hara Kebab (4pcs)</span><span class="item-price">6.9</span><span class="item-desc">Fresh baby spinach, ricotta cheese, mash potatoes, ginger</span></div>
      <div class="item"><span class="item-name">Tandoori Fool (5pcs)</span><span class="item-price">6.9</span><span class="item-desc">Crispy tangy mustard flavoured cheddar, cauliflower, broccoli</span></div>
      <div class="item"><span class="item-name">Tandoori Mushrooms (4pcs)</span><span class="item-price">7.9</span><span class="item-desc">Cup mushroom, yogurt spice, cheese, fresh mint, capsicum</span></div>
      <div class="item"><span class="item-name">Momos (6pcs)</span><span class="item-price">6.9</span><span class="item-desc">Vegetable stuffed pastry, steamed, homemade chilli sauce</span></div>
      <div class="item"><span class="item-name">Tandoori Momos (6pcs)</span><span class="item-price">7.9</span><span class="item-desc">Vegetable momos, yoghurt, ginger, garlic, cooked in clay oven</span></div>
      <div class="item"><span class="item-name">Mushrooms Momos (6pcs)</span><span class="item-price">6.9</span><span class="item-desc">Pastry stuffed with mushrooms, steamed, chilli sauce</span></div>
      <div class="item"><span class="item-name">Paneer Tikka (4pcs)</span><span class="item-price">7.9</span><span class="item-desc">Cottage cheese, gram flour, mint chilli flavoured yogurt</span></div>
      <div class="item"><span class="item-name">Kabuli Tiki (4pcs)</span><span class="item-price">6.9</span><span class="item-desc">Chickpeas, mince raw mango powder, green sultana</span></div>
      <div class="item"><span class="item-name">Samosa Chat (2pcs)</span><span class="item-price">6.9</span><span class="item-desc">Crispy pastry stuffed potatoes, peas on chickpeas</span></div>
      <div class="item"><span class="item-name">Aloo Tikki Chat (2pcs)</span><span class="item-price">6.9</span><span class="item-desc">Potato patty, fresh coriander, cumin seed, pea flour</span></div>
      <div class="item"><span class="item-name">Dhai Bhalla Papdi</span><span class="item-price">6.9</span><span class="item-desc">Crispy pastry, lentil dumpling, yogurt, date and mint chutney</span></div>
      <div class="dish" style="width:150px;height:80px" role="img" aria-label="Photo of tandoori momos on a plate with salad"></div>
    </div>
  </article>

  <article class="page page--cover">
    <div class="cover-motif" role="img" aria-label="Line illustration of a domed palace with flag brush stroke"></div>
    <div class="brand-name">Spices of Sarani Restaurant</div>
    <div class="menu-row">
      <div class="utensil" role="img" aria-label="Green fork illustration"></div>
      <div class="menu-word">Menu</div>
      <div class="utensil" role="img" aria-label="Green spoon illustration"></div>
    </div>
    <div class="veg-label"><strong>100%</strong>Vegetarian</div>
  </article>
</section>

<section class="spread spread--inner">
  <article class="page page--left">
    <div class="column">
      <h2 class="section-title">Pizza</h2>
      <p class="section-note">Medium size</p>
      <div class="item"><span class="item-name">Tropicana</span><span class="item-price">11.9</span><span class="item-desc">Pineapple, capsicum, marjoram, pitted black olive, tomato, cheese</span></div>
      <div class="item"><span class="item-name">Mexicana</span><span class="item-price">12.9</span><span class="item-desc">Jalapeño, capsicum, tomato, mushrooms, basil, olive, cheese</span></div>
      <div class="item"><span class="item-name">Kalamata</span><span class="item-price">12.9</span><span class="item-desc">Greek cheese, capsicum, red kalamata olives, onion, tomato</span></div>
      <div class="item"><span class="item-name">Siciliana</span><span class="item-price">12.9</span><span class="item-desc">Sun dry tomato, green olive, artichoke, fresh parsley, cheese</span></div>
      <div class="item"><span class="item-name">Indiana</span><span class="item-price">12.9</span><span class="item-desc">Cottage cheese, tomato, capsicum, onion, cheese</span></div>
      <div class="dish" style="width:110px;height:60px" role="img" aria-label="Photo of a vegetable pizza"></div>
      <h2 class="section-title">Dakshani Dhum</h2>
      <p class="section-note">Served with sambar, coconut chutney and tomato chilli chutney</p>
      <div class="item"><span class="item-name">Rava Dosa</span><span class="item-price">10.9</span><span class="item-desc">Crispy crepe made with ground rice and lentils, gluten free</span></div>
      <div class="item"><span class="item-name">Erulli Rava Dosa</span><span class="item-price">11.9</span><span class="item-desc">Crispy crepe with ground rice and lentil, stuffed potatoes</span></div>
      <div class="item"><span class="item-name">Plain Dosa</span><span class="item-price">10.9</span><span class="item-desc">Crispy crepe made with rice and lentil batter with butter</span></div>
      <div class="item"><span class="item-name">Udupi Masala Dosa</span><span class="item-price">11.9</span><span class="item-desc">Rice and lentil batter crepe stuffed with potatoes</span></div>
      <div class="item"><span class="item-name">Paneer Dosa</span><span class="item-price">12.9</span><span class="item-desc">Ricotta cheese, mustard seeds, chilli, curry leaf, onion, tomato</span></div>
      <div class="item"><span class="item-name">Vada Sambar (2pcs)</span><span class="item-price">6.9</span><span class="item-desc">Lentil dumpling deep fry</span></div>
      <div class="item"><span class="item-name">Thair Vada (2pcs)</span><span class="item-price">6.9</span><span class="item-desc">Lentil dumpling deep fry in yogurt buttermilk</span></div>
      <div class="item"><span class="item-name">Dhai Idly (2pcs)</span><span class="item-price">6.9</span><span class="item-desc">Dumpling of black lentil and rice, fermented, yogurt</span></div>
      <div class="item"><span class="item-name">Idly (2pcs) One Each</span><span class="item-price">6.9</span><span class="item-desc">Dumpling of black lentil and rice, steamed</span></div>
      <div class="item"><span class="item-name">Vada And Idly Plate</span><span class="item-price">8.9</span><span class="item-desc">Lentil and rice dumpling</span></div>
      <div class="spacer"></div>
      <div class="dish" style="width:110px;height:60px" role="img" aria-label="Photo of a dosa with chutney"></div>
    </div>
    <div class="column">
      <h2 class="section-title">Burger Parade</h2>
      <p class="section-note">Served with spicy potatoes fries</p>
      <div class="item"><span class="item-name">Grass Hopper</span><span class="item-price">7.9</span><span class="item-desc">Vegetables potato patty, beetroot, carrot, onion, lettuce</span></div>
      <div class="item"><span class="item-name">Cheese Hopper</span><span class="item-price">7.9</span><span class="item-desc">Potato cottage cheese patty, tomato, capsicum, lettuce</span></div>
      <div class="dish dish--green" style="width:100px;height:80px" role="img" aria-label="Photo of a vegetable burger"></div>
      <h2 class="section-title">Gujrati Masti</h2>
      <div class="item"><span class="item-name">Sev Batata Puri (6pcs)</span><span class="item-price">5.9</span><span class="item-desc">Fried puff balls with potatoes, onion, yogurt, date and mint chutney</span></div>
      <div class="item"><span class="item-name">Sev Khaman Dhokla (4pcs)</span><span class="item-price">6.9</span><span class="item-desc">Fluffy soft cake, soak and crushed lentil</span></div>
      <div class="item"><span class="item-name">Bhel Puri</span><span class="item-price">6.9</span><span class="item-desc">Rice puff, fresh green chilli, madras onion, fresh tomatoes</span></div>
      <div class="item"><span class="item-name">Kothimbir Vadi (4pcs)</span><span class="item-price">6.9</span><span class="item-desc">Fresh long coriander, gram flour, yogurt, sesame seed</span></div>
      <div class="dish dish--green" style="width:130px;height:80px" role="img" aria-label="Photo of dhokla squares in a bowl"></div>
      <h2 class="section-title">All Time<br>Favourite</h2>
      <div class="item"><span class="item-name">Channa Bhatura (2pcs)</span><span class="item-price">9.9</span><span class="item-desc">Chickpeas, onion, tomato, ginger, fresh coriander, fried bread, pickle</span></div>
    </div>
  </article>

  <article class="page">
    <div class="column">
      <h2 class="section-title">Terai Junction</h2>
      <p class="section-note">(Indo-Chinese)</p>
      <div class="item"><span class="item-name">Chow Mein</span><span class="item-price">12.9</span><span class="item-desc">Asian noodle, capsicum, cabbage, carrot, onion, garlic</span></div>
      <div class="item"><span class="item-name">Chilli Paneer</span><span class="item-price">12.9</span><span class="item-desc">Cottage cheese, capsicum, green chilli, onion, carrots</span></div>
      <div class="item"><span class="item-name">Chilli Mushrooms</span><span class="item-price">12.9</span><span class="item-desc">Button mushrooms, capsicum, red fresh chilli, onion, soya</span></div>
      <div class="item"><span class="item-name">Momos (6pcs)</span><span class="item-price">6.9</span><span class="item-desc">Vegetables stuffed pastry, steamed, chilli sauce</span></div>
      <div class="item"><span class="item-name">Cauliflower Manchurian</span><span class="item-price">12.9</span><span class="item-desc">Battered cauliflower, soya and sauce</span></div>
      <div class="item"><span class="item-name">Chilli Honey Dry</span><span class="item-price">8.9</span><span class="item-desc">Cauliflower, red capsicum, green capsicum, onion, soya</span></div>
      <div class="item"><span class="item-name">Manchurain Veg Balls</span><span class="item-price">19.9</span><span class="item-desc">Vegetarian ball made with soya and sauce</span></div>
      <div class="item"><span class="item-name">Vegetable Spring Roll (2pcs)</span><span class="item-price">6.9</span><span class="item-desc">Vegetable stuffed in pastry, soya chilli</span></div>
      <div class="item"><span class="item-name">Chilli Mushrooms Dry (8pcs)</span><span class="item-price">7.9</span><span class="item-desc">Button mushrooms, chilli, soya, capsicum, onion</span></div>
      <div class="item"><span class="item-name">Chilli Soya Paneer Dry</span><span class="item-price">10.9</span><span class="item-desc">Cottage cheese cubes, battered soya, red green capsicum</span></div>
      <div class="item"><span class="item-name">Tofu Dry</span><span class="item-price">12.9</span><span class="item-desc">Tofu fried, soya sauce, chilli sauce, bean sprout, capsicum</span></div>
      <div class="item"><span class="item-name">Vegetable Fried Rice</span><span class="item-price">12.9</span><span class="item-desc">Fresh vegetable, soya sauce, chilli sauce</span></div>
      <div class="dish dish--brown" style="width:90px;height:60px" role="img" aria-label="Photo of vegetable manchurian balls in sauce"></div>
      <h2 class="section-title">Mains</h2>
      <div class="item"><span class="item-name">Paneer Kaliyan</span><span class="item-price">20.9</span><span class="item-desc">Ricotta cheese, cashew nut, saffron, creamy gravy</span></div>
      <div class="item"><span class="item-name">Awadhi Kofta (4pcs)</span><span class="item-price">21.9</span><span class="item-desc">Gravy based nuts cream, tempered spinach, ricotta cheese</span></div>
      <div class="item"><span class="item-name">Paneer Kuchran</span><span class="item-price">19.9</span><span class="item-desc">Cottage cheese, red onion, capsicum, tomato, ginger, garlic</span></div>
      <div class="item"><span class="item-name">Mattar Paneer</span><span class="item-price">19.9</span><span class="item-desc">Cottage cheese cubes, baby peas, onion, tomato, ginger</span></div>
      <div class="item"><span class="item-name">Paneer Pasanda (2pcs)</span><span class="item-price">21.9</span><span class="item-desc">Cottage cheese sandwich, nut creamy gravy, ginger, garlic</span></div>
      <div class="item"><span class="item-name">Palak Paneer</span><span class="item-price">19.9</span><span class="item-desc">Cottage cheese cubes, baby spinach, onion, tomato, ginger</span></div>
      <div class="item"><span class="item-name">Karahi Paneer</span><span class="item-price">19.9</span><span class="item-desc">Cottage cheese cubes tossed with capsicum, onion, tomatoes</span></div>
    </div>
    <div class="column">
      <div class="item"><span class="item-name">Pindi Chana</span><span class="item-price">6.9</span><span class="item-desc">Chickpeas, onion, tomato, green chilli, lemon, ginger</span></div>
      <div class="item"><span class="item-name">Dal Tarka</span><span class="item-price">15.9</span><span class="item-desc">Yellow split peas, onion, tomato, ginger, garlic</span></div>
      <div class="item"><span class="item-name">Handi Ki Dal Makhani</span><span class="item-price">15.9</span><span class="item-desc">Black whole lentil, onion, tomato, ginger, cream, butter</span></div>
      <div class="item"><span class="item-name">Rajmaha Masala</span><span class="item-price">15.9</span><span class="item-desc">Kidney beans, onion, ginger, garlic, fresh coriander, tomatoes</span></div>
      <div class="item"><span class="item-name">Kadi Pakora</span><span class="item-price">16.9</span><span class="item-desc">Butter milk, gram flour, mustard, curry leafs, whole red chilli</span></div>
      <div class="item"><span class="item-name">Khumb Hara Piyaz</span><span class="item-price">16.9</span><span class="item-desc">Mushrooms, spring onion, ginger, garlic, tomatoes, spice</span></div>
      <div class="item"><span class="item-name">Sabzi Tarkari</span><span class="item-price">15.9</span><span class="item-desc">Melange of seasonal vegetable, beans, cauliflower, carrot</span></div>
      <div class="item"><span class="item-name">Palak Paneer</span><span class="item-price">19.9</span><span class="item-desc">Cottage cheese, baby spinach, tomatoes, ginger, garlic, cream</span></div>
      <div class="item"><span class="item-name">Paneer Tikka Masala</span><span class="item-price">19.9</span><span class="item-desc">Cottage cheese cubes, clay oven cooked, onion, capsicum</span></div>
      <div class="item"><span class="item-name">Khumb Mattar</span><span class="item-price">17.9</span><span class="item-desc">Mushrooms, peas, tomatoes, spice, ginger, garlic</span></div>
      <div class="item"><span class="item-name">Dam Aloo Kasmiri</span><span class="item-price">18.9</span><span class="item-desc">Stuffed baby potatoes, cashew nut, sultana, coconut gravy</span></div>
      <div class="item"><span class="item-name">Bhindi Do Pyaz</span><span class="item-price">15.9</span><span class="item-desc">Okra made with onion, tomato, spice, ginger, garlic</span></div>
      <div class="item"><span class="item-name">Vendakka</span><span class="item-price">15.9</span><span class="item-desc">Okra cut, fenugreek seeds, coconut cream, mustard seeds</span></div>
      <div class="item"><span class="item-name">Kathal Tarkari (Seasonal)</span><span class="item-price">19.9</span><span class="item-desc">Fresh jackfruit cooked with tomatoes, ginger, garlic</span></div>
      <div class="item"><span class="item-name">Baingan Bhartha</span><span class="item-price">16.9</span><span class="item-desc">Eggplant pulp, tomato, fresh coriander, ginger, garlic</span></div>
      <div class="item"><span class="item-name">Paneer Makhani (Nuts)</span><span class="item-price">19.9</span><span class="item-desc">Cottage cheese, butter sauce, nuts, cream, tomato</span></div>
      <div class="item"><span class="item-name">Sarso Ka Saag</span><span class="item-price">15.9</span><span class="item-desc">Fine crushed mustard leafs, onion, garlic, ginger</span></div>
      <div class="item"><span class="item-name">Bagare Baingan (Seasonal)</span><span class="item-price">16.9</span><span class="item-desc">Baby eggplant, spiced stuffed, tomato, ginger, garlic</span></div>
      <div class="item"><span class="item-name">Vegetable Korma</span><span class="item-price">16.9</span><span class="item-desc">Fresh mix vegetable in creamy nut gravy</span></div>
      <div class="item"><span class="item-name">Appam Korma</span><span class="item-price">16.9</span><span class="item-desc">Fresh mix vegetable, coconut milk, curry leafs, mustard</span></div>
      <div class="item"><span class="item-name">Bharela Karela</span><span class="item-price">16.9</span><span class="item-desc">Bitter gourd stuffed potatoes, spice, onion, ginger, garlic</span></div>
      <div class="spacer"></div>
      <div class="dish" style="width:130px;height:70px" role="img" aria-label="Photo of a bowl of paneer curry"></div>
    </div>
  </article>
</section>

</body>
</html>
```